Aircraft maintenance buisness card

I am an aircraft mechanic looking for a personal buisness card . I would like my name and a title of Aircraft Maintenance Manager . I would like a suttle picture of an aircraft and helicopter .

elegant and professional wtih my contact .

My name should be on the car and Aircraft Maintenance Manager under with my contact infor below .

i have attached some pictures but i am open to other pics and ideas . I would like a airliner or private jet and a helicopter in the picture . The Images should be suttle and not the main idea . I also uploaded a picture of a jet engine which is cool . Be creative and i will work with you to finalize something .
Updates

Project Deadline Extended
Reason: Looking for more variations . Very good so far but looiking for a bit more styles and i uploaded my logo that i purchased . Please use my logo and be creative with it . I like some variations of black card with maybe some pictures that i uploaded but i am open to ideas . Be creative and i will work with you .

Project Deadline Extended
Reason: Looking for more designs and variations . Not yet satisfied with the designs i have gotten .

Industry/Entity Type

Aviation

Contact Information for Business Card

Aircraft Maintenance Manager

Font styles to use
Serif

Colors

Designer to choose colors to be used in the design.

Requirements
Must have
• An aviation related Logo if possible incorporated in the card possibly
• My name
• Tobias Marven Ellery
• 482 Pellow Ave.
• Brackton , VT
• 07519
• Email: Tmskyworks@quillmail.net
Nice to have
• Suttle Backround of a Private Jet or Airliner and a Helicopter .

```html
<!DOCTYPE html>
<html lang="en">
<head>
<meta charset="utf-8">
<title>Tobias Marven Ellery – Business Card</title>
<link rel="stylesheet" href="https://fonts.googleapis.com/css2?family=Cinzel:wght@400;500&display=swap">
<style>
  :root {
    --backdrop: #2b2b2d;
    --card-white: #ffffff;
    --brand-blue: #1f4b9c;
    --ink-dark: #2a2a2a;
    --rock-light: #9a968e;
    --rock-mid: #77736b;
    --rock-dark: #4f4d48;
    --foliage: #4e5a44;
  }
  * { margin: 0; padding: 0; box-sizing: border-box; }
  html, body {
    width: 1200px;
    height: 1000px;
    overflow: hidden;
    background: var(--backdrop);
  }
  .canvas {
    position: relative;
    width: 1200px;
    height: 1000px;
    display: flex;
    flex-direction: column;
    align-items: center;
    justify-content: center;
    gap: 20px;
  }
  .card {
    position: relative;
    width: 820px;
    height: 470px;
    overflow: hidden;
  }
  .card-front {
    background:
      radial-gradient(ellipse at 92% 20%, var(--foliage) 0%, transparent 30%),
      radial-gradient(ellipse at 10% 95%, var(--foliage) 0%, transparent 35%),
      linear-gradient(160deg, var(--rock-light) 0%, var(--rock-mid) 45%, var(--rock-dark) 100%);
  }
  .card-back {
    background: var(--card-white);
    font-family: "Cinzel", serif;
    color: var(--ink-dark);
    text-align: center;
  }
  .holder-name {
    margin-top: 72px;
    font-size: 40px;
    font-weight: 400;
    letter-spacing: 2px;
    color: var(--brand-blue);
  }
  .holder-title {
    margin-top: 2px;
    font-size: 19px;
    letter-spacing: 1.5px;
  }
  .contact-icons {
    display: flex;
    justify-content: center;
    gap: 14px;
    margin-top: 36px;
  }
  .contact-icons svg { width: 30px; height: 30px; }
  .phone {
    margin-top: 18px;
    font-size: 32px;
    letter-spacing: 2px;
    color: var(--brand-blue);
  }
  .email, .website {
    font-size: 20px;
    letter-spacing: 2px;
    line-height: 1.35;
  }
  .website .domain { color: var(--brand-blue); }
  .address {
    margin-top: 26px;
    font-size: 20px;
    letter-spacing: 3px;
  }
  .accent-band {
    position: absolute;
    left: 0; right: 0; bottom: 0;
    height: 14px;
    background: var(--brand-blue);
  }
</style>
</head>
<body>
<main class="canvas">
  <section class="card card-front" role="img" aria-label="Photograph of a blue and white helicopter flying in front of a grey granite cliff face"></section>

  <section class="card card-back">
    <h1 class="holder-name">Tobias Marven Ellery</h1>
    <p class="holder-title">Aircraft Maintenance Manager</p>

    <div class="contact-icons" aria-hidden="true">
      <svg viewBox="0 0 30 30" class="icon-phone">
        <circle cx="15" cy="15" r="13" fill="none" stroke="var(--brand-blue)" stroke-width="1.6"/>
        <path d="M10.5 9.5c.8-.8 1.6-.6 2 .1l1.1 2c.3.6.1 1.1-.4 1.5l-.6.5c.6 1.4 1.6 2.5 3 3.1l.5-.6c.4-.5 1-.7 1.5-.4l2 1.1c.7.4.9 1.2.1 2-.9.9-2 1.3-3.3.8-3.1-1.2-5.4-3.5-6.6-6.6-.5-1.300-.1-2.4.7-3.5z" fill="var(--brand-blue)"/>
      </svg>
      <svg viewBox="0 0 30 30" class="icon-mail">
        <circle cx="15" cy="15" r="13" fill="none" stroke="var(--brand-blue)" stroke-width="1.6"/>
        <rect x="8.5" y="10.5" width="13" height="9" fill="var(--brand-blue)"/>
        <path d="M8.5 10.5l6.5 5 6.5-5" fill="none" stroke="#fff" stroke-width="1.2"/>
      </svg>
      <svg viewBox="0 0 30 30" class="icon-web">
        <circle cx="15" cy="15" r="13" fill="none" stroke="var(--brand-blue)" stroke-width="1.6"/>
        <circle cx="15" cy="15" r="7" fill="var(--brand-blue)"/>
        <path d="M8 15h14M15 8v14M10 11h10M10 19h10" stroke="#fff" stroke-width="0.8"/>
        <ellipse cx="15" cy="15" rx="3" ry="7" fill="none" stroke="#fff" stroke-width="0.8"/>
      </svg>
    </div>

    <p class="phone">000 555 812 406</p>
    <p class="email">Tmskyworks@quillmail.net</p>
    <p class="website">www.<span class="domain">marvenaero</span>.com</p>
    <p class="address">482 Pellow Ave. Brackton , VT 07519</p>

    <div class="accent-band"></div>
  </section>
</main>
</body>
</html>
```